Hold Each Morning As A MOSSbright Harbour

Hello Designers! We need a captivating notebook cover design for our self-development company for people with disabilities. We help people with a diagnosis see everyday as a great adventure than something to ensure. This notebook is to capture the brightness and positivity of everyday, that your struggles are meant for you to overcome. We would like to see designs that follow with our brand (uploaded) and I've also added our logo and kind of notebook as a guide. The final design should be inviting and bright. Use the title "Keep Each Morning A Quiet Lantern". Will decide the words once the background design is finalized

Notebook Size: 8.5 x 5.75 inches
Updates

Hello Designers! I'm extending the deadline to give you an opportunity to submit different and unique designs for the MOSSbright HARBOUR Journal. I've given feedback to most of you so this is your opportunity to try something new. Looking for clean, inviting and unique designs that use the logo colour scheme (attached -- navy blue, light blue, yellow, black). Preferably front and back cover designs.

Target Market(s)

Between 25-35 years

Font styles to use
Serif
Sans Serif
Decorative
Script

Colors
0255a3
fbed22

Requirements
Must have
• -Use colour scheme as per attachment as main colours (can go beyond for contrast ex. pinks/purples/indigo/etc)
Nice to have
• Would like to see designs related to nature, art and/or graphic prints.
Should not have
• icons (no stick figures), silhouettes of people, no hands
• NO stock images

```html
<!DOCTYPE html>
<html lang="en">
<head>
<meta charset="UTF-8">
<title>Keep Each Morning A Quiet Lantern — Journal Cover</title>
<link href="https://fonts.googleapis.com/css2?family=Caveat+Brush&display=swap" rel="stylesheet">
<style>
  :root {
    --page: #ffffff;
    --night-top: #04081a;
    --night-mid: #0c1f55;
    --night-low: #1d3f8f;
    --dawn: #6f97cc;
    --star-gold: #f6c41a;
  }
  html, body {
    margin: 0;
    padding: 0;
    width: 900px;
    height: 1200px;
    overflow: hidden;
    background: var(--page);
  }
  .canvas {
    position: relative;
    width: 900px;
    height: 1200px;
    background: var(--page);
  }
  .journal-cover {
    position: absolute;
    left: 169px;
    top: 160px;
    width: 586px;
    height: 867px;
    overflow: hidden;
    background: linear-gradient(to bottom,
      var(--night-top) 0%,
      #081640 30%,
      var(--night-mid) 55%,
      var(--night-low) 78%,
      var(--dawn) 100%);
  }
  .sky-grain,
  .sky-stars {
    position: absolute;
    inset: 0;
    width: 100%;
    height: 100%;
  }
  .sky-grain { mix-blend-mode: screen; opacity: 0.35; }
  .cover-title {
    position: absolute;
    left: 0;
    right: 0;
    top: 140px;
    margin: 0;
    text-align: center;
    font-family: "Caveat Brush", cursive;
    font-weight: 400;
    color: var(--star-gold);
    text-transform: uppercase;
    line-height: 1;
    letter-spacing: 0.5px;
  }
  .cover-title .title-line { display: block; }
  .cover-title .title-line--first { font-size: 50px; }
  .cover-title .title-line--second { font-size: 62px; margin-top: 10px; }
</style>
</head>
<body>
<main class="canvas">
  <section class="journal-cover">
    <svg class="sky-grain" viewBox="0 0 586 867" preserveAspectRatio="none" aria-hidden="true">
      <defs>
        <filter id="grain">
          <feTurbulence type="fractalNoise" baseFrequency="0.9" numOctaves="2" stitchTiles="stitch"/>
          <feColorMatrix type="matrix" values="0 0 0 0 0.55  0 0 0 0 0.65  0 0 0 0 0.85  0 0 0 1.4 -0.55"/>
        </filter>
        <linearGradient id="grain-fade" x1="0" y1="0" x2="0" y2="1">
          <stop offset="0" stop-color="#fff" stop-opacity="0.1"/>
          <stop offset="1" stop-color="#fff" stop-opacity="1"/>
        </linearGradient>
        <mask id="grain-mask">
          <rect width="586" height="867" fill="url(#grain-fade)"/>
        </mask>
      </defs>
      <rect width="586" height="867" filter="url(#grain)" mask="url(#grain-mask)"/>
    </svg>

    <svg class="sky-stars" viewBox="0 0 586 867" aria-hidden="true">
      <defs>
        <polygon id="star" points="0,-5 1.2,-1.6 4.8,-1.5 1.9,0.7 2.9,4.1 0,2 -2.9,4.1 -1.9,0.7 -4.8,-1.5 -1.2,-1.6" fill="var(--star-gold)"/>
      </defs>
      <path class="shooting-star-trail" d="M193,123 Q100,150 70,248" fill="none" stroke="var(--star-gold)" stroke-width="1" stroke-dasharray="1.5 2" opacity="0.8"/>
      <use href="#star" x="72" y="78"/>
      <use href="#star" x="358" y="76"/>
      <use href="#star" x="249" y="130"/>
      <use href="#star" x="459" y="162"/>
      <use href="#star" x="534" y="221"/>
      <use href="#star" x="67" y="253"/>
    </svg>

    <h1 class="cover-title">
      <span class="title-line title-line--first">Keep Each Morning</span>
      <span class="title-line title-line--second">A Quiet Lantern</span>
    </h1>
  </section>
</main>
</body>
</html>
```